R.Morton LLC Organizational Change and Development

I am starting my own company as a a senior facilitator, keynote speaker, executive coach, webinar training instructor, quality management adviser, and classroom presenter. I have taught diversity and cultural competence, organizational development, change management, leadership, organizational dynamics, team-building, accountability, negotiation, work-life balance, quality management, DISC, and hundreds of web based trainings. I have a PhD. in Counseling Psychology, MBA, B.S. in Human Development, Family Studies, and a Master’s Practitioner of Neurolinguistic Programming. My degrees and certifications give me a foundation for advising a wide variety of people, industries, and cultures at all organizational levels. I would like a design that's fun, engaging, humorous, progressive, and has a professional feel. I really like the colors burgundy wine.

Target Market(s)

corporate America

Industry/Entity Type

Training

Number of Pages Required

5+ page

Colors
eb1f26
f04a50
3176b4
33a6d7

Requirements
Must have
• my different areas of expertise - fun visuals -easy for me to use
Should not have
• something that looks stiff, too traditional or boring

```html
<!DOCTYPE html>
<html lang="en">
<head>
<meta charset="utf-8">
<title>R.Morton LLC — Organizational Change and Development</title>
<link href="https://fonts.googleapis.com/css2?family=Nunito+Sans:wght@300;400;600;700&display=swap" rel="stylesheet">
<style>
  :root{
    --burgundy:#7d1a22;
    --red:#eb1f26;
    --red-light:#f04a50;
    --blue:#3176b4;
    --blue-light:#33a6d7;
    --header-bg:#fdfbf5;
    --footer-bg:#f1f1f1;
    --ink:#2b2b2b;
    --body-text:#666;
    --rule:#d9d9d9;
  }
  *{box-sizing:border-box;margin:0;padding:0}
  html,body{width:959px;height:1200px;overflow:hidden;background:#fff}
  body{font-family:"Nunito Sans",sans-serif;color:var(--ink);position:relative}
  .abs{position:absolute}

  /* header */
  .site-header{position:absolute;left:0;top:0;width:959px;height:92px;background:var(--header-bg)}
  .brand{position:absolute;left:120px;top:20px}
  .brand-name{font-size:40px;font-weight:400;color:var(--burgundy);letter-spacing:1px;line-height:1}
  .brand-tagline{font-size:5px;color:#999;letter-spacing:.6px;margin:4px 0 0 42px}
  .phone{position:absolute;left:668px;top:11px;font-size:19px;color:#333;display:flex;align-items:center;gap:6px}
  .main-nav{position:absolute;top:50px;left:524px;display:flex;align-items:center;font-size:13px}
  .main-nav a{color:#222;text-decoration:none;padding:0 13px;line-height:30px}
  .main-nav a.active{background:linear-gradient(var(--blue-light),var(--blue));color:#fff;border-radius:2px;padding:0 17px;margin-right:0}

  /* hero */
  .hero{position:absolute;left:0;top:92px;width:959px;height:415px;
    background:radial-gradient(ellipse at 48% 85%,#f0b868 0%,#d89a55 25%,#a57a4e 50%,#5b3a20 78%,#2a1608 100%)}
  .hero-portrait{position:absolute;left:580px;top:28px;width:250px;height:387px;
    background:linear-gradient(#e7c98a 0%,#d8b074 28%,#1a1a22 38%,#0d0d14 100%);border-radius:110px 110px 0 0;opacity:.92}
  .hero-title{position:absolute;left:136px;top:178px;font-size:28px;font-weight:400;color:#fff}
  .hero-sub{position:absolute;left:138px;top:224px;font-size:12.5px;letter-spacing:3px;color:#fff;font-weight:600}
  .slider-arrows{position:absolute;left:178px;top:365px;width:46px;height:33px;background:rgba(80,60,40,.7)}

  /* welcome */
  .welcome{position:absolute;left:0;top:516px;width:959px;text-align:center}
  .welcome h1{font-size:26px;font-weight:400;letter-spacing:.5px;color:#333}
  .welcome h2{font-size:13.5px;font-weight:600;color:#333;margin-top:1px}
  .welcome p{width:700px;margin:10px auto 0;font-size:10.5px;line-height:14.5px;color:var(--body-text)}
  .btn{display:inline-block;font-size:11.5px;color:#fff;line-height:30px;padding:0 10px;border-radius:2px;
    background:linear-gradient(var(--blue-light),var(--blue))}
  .btn.alt{background:linear-gradient(var(--red-light),var(--red))}
  .welcome .btn{margin-top:10px;padding:0 10px}
  .rule{position:absolute;left:105px;width:747px;height:1px;background:var(--rule)}

  /* services */
  .service{position:absolute;width:240px;height:140px;
    background:linear-gradient(160deg,#fff 70%,#ececec 100%)}
  .service h3{font-size:13.5px;font-weight:600;color:#333}
  .service p{font-size:11px;line-height:14.5px;color:var(--body-text);margin:10px 0 11px;text-align:justify}

  /* footer */
  .site-footer{position:absolute;left:0;top:984px;width:959px;height:216px;background:var(--footer-bg)}
  .footer-title{position:absolute;font-size:15px;font-weight:400;color:#333}
  .footer-links{position:absolute;left:105px;top:62px;list-style:none;font-size:11.5px;line-height:19px}
  .subscribe-input{position:absolute;left:271px;top:61px;width:161px;height:32px;background:#fff;border:1px solid #ddd;
    font-size:10.5px;color:#555;padding:9px 11px}
  .subscribe-go{position:absolute;left:431px;top:55px;width:39px;height:44px;border-radius:3px;
    background:linear-gradient(var(--blue-light),var(--blue));color:#fff;font-size:11px;text-align:center;line-height:44px}
  .social{position:absolute;top:154px;width:29px;height:29px}
  .contact-lines{position:absolute;left:543px;top:62px;font-size:11px;line-height:19.3px;color:#222}
  .map{position:absolute;left:676px;top:58px;width:156px;height:78px;background:linear-gradient(135deg,#e4dcc6,#d7d3b3)}
  .copyright{position:absolute;left:676px;top:173px;font-size:10px;color:#444}
</style>
</head>
<body>

<header class="site-header">
  <div class="brand">
    <div class="brand-name">R.MORTON</div>
    <div class="brand-tagline">ORGANIZATIONAL CHANGE AND DEVELOPMENT</div>
  </div>
  <div class="phone">
    <svg width="16" height="16" viewBox="0 0 24 24" aria-hidden="true"><path fill="#333" d="M6.6 10.8a15.1 15.1 0 0 0 6.6 6.6l2.2-2.2a1 1 0 0 1 1-.25 11.4 11.4 0 0 0 3.6.57 1 1 0 0 1 1 1V20a1 1 0 0 1-1 1A17 17 0 0 1 3 4a1 1 0 0 1 1-1h3.5a1 1 0 0 1 1 1c0 1.25.2 2.45.57 3.57a1 1 0 0 1-.25 1z"/></svg>
    (555) 214 - 0398
  </div>
  <nav class="main-nav">
    <a class="active">Home</a><a>About Us</a><a>Services</a><a>Contact Us</a>
  </nav>
</header>

<section class="hero">
  <div class="hero-portrait" role="img" aria-label="Portrait photo of the consultant, arms crossed, in a dark blazer"></div>
  <div class="hero-title">PhD. in Counseling Psychology</div>
  <div class="hero-sub">MBA in Human Development &amp; Family Studies</div>
  <div class="slider-arrows">
    <svg width="46" height="33" viewBox="0 0 46 33" aria-hidden="true"><path d="M19 10l-6 6.5 6 6.5M27 10l6 6.5-6 6.5" stroke="#fff" stroke-width="2" fill="none"/></svg>
  </div>
</section>

<section class="welcome">
  <h1>WELCOME</h1>
  <h2>Home Content</h2>
  <p>Nemo enim ipsam voluptatem quia voluptas sit aspernatur aut odit aut fugit, sed quia consequuntur magni dolores eos qui ratione voluptatem sequi nesciunt. Neque porro quisquam est, qui dolorem ipsum quia dolor sit amet, consectetur, adipisci velit, sed quia non numquam eius modi tempora incidunt</p>
  <span class="btn">Read more</span>
</section>

<div class="rule" style="top:663px"></div>

<article class="service" style="left:108px;top:684px"><h3>Senior facilitator</h3><p>Nemo enim ipsam voluptatem quia voluptas sit aspernatur aut odit aut fugit, sed quia consequuntur magni dolores eos qui ratione voluptatem sequi nesciunt.</p><span class="btn alt">Read more</span></article>
<article class="service" style="left:363px;top:682px"><h3>Keynote speaker</h3><p>Nemo enim ipsam voluptatem quia voluptas sit aspernatur aut odit aut fugit, sed quia consequuntur magni dolores eos qui ratione voluptatem sequi nesciunt.</p><span class="btn">Read more</span></article>
<article class="service" style="left:619px;top:686px"><h3>Executive coach</h3><p>Nemo enim ipsam voluptatem quia voluptas sit aspernatur aut odit aut fugit, sed quia consequuntur magni dolores eos qui ratione voluptatem sequi nesciunt.</p><span class="btn">Read more</span></article>
<article class="service" style="left:106px;top:830px"><h3>Webinar training instructor</h3><p>Nemo enim ipsam voluptatem quia voluptas sit aspernatur aut odit aut fugit, sed quia consequuntur magni dolores eos qui ratione voluptatem sequi nesciunt.</p><span class="btn">Read more</span></article>
<article class="service" style="left:363px;top:832px"><h3>Quality management adviser</h3><p>Nemo enim ipsam voluptatem quia voluptas sit aspernatur aut odit aut fugit, sed quia consequuntur magni dolores eos qui ratione voluptatem sequi nesciunt.</p><span class="btn">Read more</span></article>
<article class="service" style="left:619px;top:833px"><h3>Classroom presenter</h3><p>Nemo enim ipsam voluptatem quia voluptas sit aspernatur aut odit aut fugit, sed quia consequuntur magni dolores eos qui ratione voluptatem sequi nesciunt.</p><span class="btn">Read more</span></article>

<footer class="site-footer">
  <div class="footer-title" style="left:101px;top:28px">Quick Links</div>
  <ul class="footer-links"><li>Home</li><li>About Us</li><li>Services</li><li>Contact Us</li></ul>

  <div class="footer-title" style="left:268px;top:30px">Subscribe Newsletter</div>
  <div class="subscribe-input">Email Id</div>
  <div class="subscribe-go">GO</div>

  <div class="footer-title" style="left:272px;top:123px">Follow Us</div>
  <div class="social" style="left:272px;background:#1e6f8c" role="img" aria-label="Social network link"></div>
  <div class="social" style="left:306px;background:#e31b23" role="img" aria-label="Social network link"></div>
  <div class="social" style="left:341px;background:#2a8ac0" role="img" aria-label="Social network link"></div>

  <div class="footer-title" style="left:543px;top:31px">Contact</div>
  <div class="contact-lines">Suite 4, Harbour Point<br>Phone: +64 9 555 0142<br>17 Kestrel Lane<br>Northvale</div>
  <div class="map" role="img" aria-label="Street map of the office location"></div>

  <div class="copyright">© 2014.www.mortonchange.com</div>
</footer>

</body>
</html>
```